TBrandow executive consulting

We need a basic clean website for executive consulting. Rosalind is the previos CIO for bluecrest skyways and currently supports several technology companies with innovation and transformation.

Target Market(s)

C level technology and CIO training

Industry/Entity Type

Technology and travel industry

Coding

Coded - Design and coding required

Number of Pages Required

3 page

Font styles to use
Sans Serif

Colors
0054AA
0677BA
7BADD7
CADEEF
E8F1F8
0094D4
00A9DD
6FCCEA
C7EBF8
E9F6FB

Requirements
Must have
• Home page, about us, services social media links

```html
<!DOCTYPE html>
<html lang="en">
<head>
<meta charset="UTF-8">
<title>TBrandow Executive Consulting</title>
<link href="https://fonts.googleapis.com/css2?family=Red+Hat+Display:ital,wght@0,400;0,500;0,700;0,800;0,900;1,500&family=Lora:ital@1&display=swap" rel="stylesheet">
<style>
:root{
  --navy:#0054AA;
  --blue:#0677BA;
  --sky:#0094D4;
  --cyan:#00A9DD;
  --teal:#4FC3B4;
  --ink:#1c1c1c;
  --text:#2b2b2b;
  --muted:#f0f3f8;
  --line:#c9d3df;
  --white:#ffffff;
  --black:#000000;
}
*{margin:0;padding:0;box-sizing:border-box}
html,body{width:1200px;height:3220px;overflow:hidden}
body{position:relative;font-family:"Red Hat Display",sans-serif;color:var(--text);background:var(--white)}
.abs{position:absolute}
a{color:inherit;text-decoration:none}

/* header */
.site-header{position:absolute;left:0;top:0;width:1200px;height:84px;background:var(--white);border-top:3px solid var(--navy)}
.brand{position:absolute;left:115px;top:16px;height:56px;display:flex;align-items:center;gap:10px;font-weight:800;font-size:44px;color:var(--blue);letter-spacing:1px}
.brand-dot{width:12px;height:12px;border-radius:50%;background:var(--cyan)}
.main-nav{position:absolute;left:400px;top:34px;display:flex;align-items:center;font-size:14px;font-weight:500;color:#333}
.main-nav a{padding:0 20px}
.main-nav .sep{color:#999}
.main-nav .active{color:var(--navy);font-weight:700;position:relative}
.main-nav .active::before{content:"";position:absolute;left:50%;top:-8px;width:3px;height:3px;background:var(--navy)}
.search-btn{position:absolute;left:888px;top:22px;width:42px;height:42px}
.btn{display:inline-flex;align-items:center;justify-content:center;background:linear-gradient(var(--sky),var(--navy));color:var(--white);font-weight:700;font-size:14px;border-radius:3px;box-shadow:0 2px 4px rgba(0,0,0,.2)}
.header-cta{position:absolute;left:960px;top:19px;width:128px;height:47px}

/* hero */
.hero{position:absolute;left:0;top:84px;width:1200px;height:712px;background:linear-gradient(90deg,#121416 0%,#1f2528 35%,#4a3d30 65%,#6b5544 100%)}
.hero-title{position:absolute;left:115px;top:150px;font-size:48px;line-height:64px;font-weight:800;color:var(--white)}
.hero-title .accent{color:var(--teal)}
.hero-title .italic{font-style:italic;font-weight:500}
.hero-cta{position:absolute;left:115px;top:383px;width:342px;height:47px}
.slider-dots{position:absolute;left:47px;top:265px;display:flex;flex-direction:column;gap:14px}
.slider-dots span{width:14px;height:14px;border:2px solid var(--white);border-radius:50%}
.slider-dots .on{width:20px;height:20px;margin-left:-3px;background:var(--white);box-shadow:inset 0 0 0 3px #333}
.wedge{position:absolute;left:0;width:1200px;height:146px}
.round-arrow{position:absolute;width:48px;height:48px;border-radius:50%;background:var(--white);border:1px dashed var(--sky);display:flex;align-items:center;justify-content:center;color:var(--navy)}

/* about */
.about-frame{position:absolute;left:115px;top:981px;width:378px;height:554px;border:8px solid var(--sky);border-top-width:8px}
.about-frame::before,.about-frame::after{content:"";position:absolute;width:16px;height:110px;background:var(--white)}
.about-frame::before{left:-12px;top:220px}
.about-frame::after{right:-12px;top:220px}
.about-photo{position:absolute;left:132px;top:950px;width:353px;height:568px;background:linear-gradient(160deg,#8f8a84 0%,#d9d2c8 40%,#1d2433 75%,#151a26 100%)}
.eyebrow{font-size:22px;font-weight:400;color:#333;text-transform:uppercase}
.section-title{font-size:40px;font-weight:900;color:var(--ink);text-transform:uppercase;line-height:1.1}
.section-title span{font-weight:400;color:var(--blue)}
.about-copy{position:absolute;left:583px;top:940px;width:485px}
.about-copy p{font-size:17px;line-height:26px;color:#222;margin-top:20px}
.about-copy .eyebrow+.section-title{margin-bottom:28px}
.about-cta{position:absolute;left:583px;top:1532px;width:129px;height:47px}

/* services */
.center-head{position:absolute;left:0;width:1200px;text-align:center}
.service-card{position:absolute;top:1905px;width:228px;height:202px;border:1px solid var(--line);background:var(--white);text-align:center;font-size:14px;font-weight:500;color:#222;line-height:19px}
.service-card .icon{width:86px;height:86px;margin:22px auto 28px;background:var(--blue);border:3px solid var(--white);outline:3px solid var(--sky);display:flex;align-items:center;justify-content:center}
.service-card.featured{top:1832px;left:358px;width:236px;height:376px;background:var(--navy);border:6px solid var(--sky);color:var(--white)}
.service-card.featured .icon{background:var(--white);outline-color:var(--white);border-color:var(--navy);margin-top:24px}
.featured .rule{width:64px;height:4px;background:var(--white);margin:20px auto 20px}
.featured p{font-size:13px;line-height:20.5px;padding:0 18px}
.featured .more{display:block;margin-top:16px;font-size:13px;text-decoration:underline}
.carousel-arrow{position:absolute;top:1994px;width:32px;height:24px}

/* testimonials */
.testimonials{position:absolute;left:0;top:2306px;width:1200px;height:640px;background:var(--muted)}
.quote-box{position:absolute;left:113px;top:2510px;width:975px;height:230px;background:var(--white);border:1px solid var(--line);text-align:center;padding:25px 45px 0}
.quote-box::after{content:"";position:absolute;left:-4px;right:-4px;bottom:-4px;height:96px;border:4px solid var(--sky);border-top:none}
.quote-box p{font-family:"Lora",serif;font-style:italic;font-size:12.2px;line-height:18px;color:#333;margin-bottom:14px}
.quote-rule{width:46px;height:3px;background:var(--navy);margin:6px auto 10px}
.quote-author{font-size:14px;color:#222}
.quote-author b{font-weight:700}
.quote-mark{position:absolute;right:78px;bottom:20px;font-size:62px;font-weight:900;color:var(--navy);line-height:40px;height:34px;overflow:hidden}

/* footer */
.site-footer{position:absolute;left:0;top:2986px;width:1200px;height:234px;background:var(--black);color:var(--white)}
.footer-brand{position:absolute;left:112px;top:74px;display:flex;align-items:center;gap:10px;font-size:44px;font-weight:800}
.footer-brand .brand-dot{background:var(--white)}
.footer-nav{position:absolute;right:112px;top:90px;display:flex;font-size:14px;font-weight:700}
.footer-nav a{padding:0 22px}
.footer-nav a:last-child{padding-right:0}
.footer-nav .sep{color:#888}
.footer-rule{position:absolute;left:73px;top:157px;width:977px;height:1px;background:#444}
.copyright{position:absolute;left:0;top:188px;width:1200px;text-align:center;font-size:13px;color:#ddd}
</style>
</head>
<body>

<header class="site-header">
  <a class="brand" href="#"><span class="brand-dot"></span>TB</a>
  <nav class="main-nav">
    <a class="active" href="#">HOME</a><span class="sep">|</span>
    <a href="#">ABOUT US</a><span class="sep">|</span>
    <a href="#">OUR SERVICES</a><span class="sep">|</span>
    <a href="#">TESTIMONIALS</a>
  </nav>
  <svg class="search-btn" viewBox="0 0 42 42" aria-label="Search">
    <polygon points="10,2 32,2 41,21 32,40 10,40 1,21" fill="none" stroke="#9aa7b5"/>
    <circle cx="19.5" cy="19.5" r="6.5" fill="none" stroke="#222" stroke-width="1.6"/>
    <line x1="24.5" y1="24.5" x2="29" y2="29" stroke="#222" stroke-width="1.8"/>
  </svg>
  <a class="btn header-cta" href="#">CONTACT US</a>
</header>

<section class="hero" role="img" aria-label="Photo of three colleagues reviewing a laptop together in an office">
  <div class="slider-dots"><span></span><span></span><span class="on"></span><span></span></div>
  <h1 class="hero-title"><span class="accent">EMPOWERING</span><br>INNOVATION,<br><span class="italic">DRIVING SUCCESS</span></h1>
  <a class="btn hero-cta" href="#">LET’S SHAPE THE FUTURE TOGETHER</a>
</section>
<svg class="wedge" style="top:650px" viewBox="0 0 1200 146" preserveAspectRatio="none">
  <polygon points="0,146 600,90 1200,146" fill="#fff"/>
  <polygon points="0,0 600,90 0,146" fill="#00A9DD"/>
  <polygon points="1200,0 600,90 1200,146" fill="#0054AA"/>
</svg>
<div class="round-arrow" style="left:576px;top:694px">
  <svg width="16" height="18" viewBox="0 0 16 18"><path d="M8 2v13M3 10l5 5 5-5" fill="none" stroke="currentColor" stroke-width="1.6"/></svg>
</div>

<section class="about">
  <div class="about-frame"></div>
  <div class="about-photo" role="img" aria-label="Portrait photo of Rosalind Brandow in a dark blazer"></div>
  <div class="about-copy">
    <div class="eyebrow">Who we are</div>
    <h2 class="section-title">About <span>Us</span></h2>
    <p>Rosalind Brandow is a seasoned leader with a remarkable 40-year career in the travel industry, including 20 transformative years at Bluecrest Skyways. As the Senior Vice President of Technology (CIO), Rosalind spearheaded some of the company’s most significant technological and strategic transformations, helping Bluecrest Skyways stay at the forefront of innovation in the competitive travel market. Her work bridged the gap between business strategy and technology, driving measurable success and resilience.</p>
    <p>With expertise in Leadership, Mentorship, Technology Strategy, and Digital Transformation, Rosalind is passionate about empowering IT leaders to forge stronger connections between their technology teams and business goals. Her approach is rooted in a belief that technology is not just a tool but a catalyst for growth, collaboration, and innovation.</p>
  </div>
  <a class="btn about-cta" href="#">LEARN MORE</a>
</section>

<section class="services">
  <div class="center-head" style="top:1694px">
    <div class="eyebrow">What we do</div>
    <h2 class="section-title">Services <span>Provide</span></h2>
  </div>

  <svg class="carousel-arrow" style="left:42px" viewBox="0 0 32 24"><path d="M30 12H3M11 4 3 12l8 8" fill="none" stroke="#222" stroke-width="1.6"/></svg>

  <div class="service-card" style="left:113px">
    <div class="icon"><svg width="48" height="48" viewBox="0 0 48 48" fill="none" stroke="#fff" stroke-width="1.8"><circle cx="14" cy="18" r="4"/><circle cx="34" cy="14" r="4"/><path d="M8 38v-9a6 6 0 0 1 12 0v9M28 38V26a6 6 0 0 1 12 0v12M6 38h36"/></svg></div>
    LEADERSHIP<br>MENTORSHIP
  </div>

  <div class="service-card featured">
    <div class="icon"><svg width="50" height="50" viewBox="0 0 50 50" fill="none" stroke="#0054AA" stroke-width="1.8"><circle cx="22" cy="25" r="12"/><circle cx="22" cy="25" r="5"/><path d="M34 19h8M34 25h10M34 31h8M42 19v-5M42 31v5"/><circle cx="42" cy="12" r="2"/><circle cx="42" cy="38" r="2"/></svg></div>
    TECHNOLOGY STRATEGY<br>DEVELOPMENT
    <div class="rule"></div>
    <p>Workshops and training sessions to strengthen collaboration between IT and business units.</p>
    <a class="more" href="#">LEARN MORE</a>
  </div>

  <div class="service-card" style="left:612px">
    <div class="icon"><svg width="48" height="48" viewBox="0 0 48 48" fill="none" stroke="#fff" stroke-width="1.8"><circle cx="20" cy="28" r="11" stroke-dasharray="4 2.5"/><circle cx="20" cy="28" r="5"/><circle cx="35" cy="14" r="6" stroke-dasharray="3 2"/><circle cx="35" cy="14" r="2"/></svg></div>
    DIGITAL TRANSFORMATION<br>CONSULTING
  </div>

  <div class="service-card" style="left:860px">
    <div class="icon"><svg width="48" height="48" viewBox="0 0 48 48" fill="none" stroke="#fff" stroke-width="1.8"><circle cx="28" cy="15" r="8" stroke-dasharray="3.5 2"/><circle cx="28" cy="15" r="3"/><path d="M6 30h8l8 3h8a2 2 0 0 1 0 4h-9M14 30v10l10 2 18-8a2 2 0 0 0-2-4l-10 4"/></svg></div>
    IT-BUSINESS PARTNERSHIP<br>DEVELOPMENT
  </div>

  <svg class="carousel-arrow" style="left:1118px" viewBox="0 0 32 24"><path d="M2 12h27M21 4l8 8-8 8" fill="none" stroke="#222" stroke-width="1.6"/></svg>
</section>

<section class="testimonials">
  <div class="center-head" style="top:104px">
    <div class="eyebrow">Testimonials</div>
    <h2 class="section-title">Clients <span>Words</span></h2>
  </div>
</section>
<div class="quote-box">
  <p>Rosalind is a decisive and fair leader who exemplifies strength, wisdom, and empathy. She always possesses a clear vision for the future and is willing to make bold decisions which are grounded in data, expertise, and intuition while remaining open to diverse perspectives.</p>
  <p>Rosalind’s leadership style fosters an inclusive environment where every voice matters, empowering her team to excel and innovate. She was able to balance ambition with humanity and succeeded in prioritizing the well-being of her people, ensuring they feel valued and supported.</p>
  <p>In times of uncertainty her unwavering confidence and fairness inspire trust, driving the organization forward with resilience and integrity.</p>
  <div class="quote-rule"></div>
  <div class="quote-author"><b>DANIEL HUGHES,</b> CEO NORVANE</div>
  <div class="quote-mark">”</div>
</div>

<svg class="wedge" style="top:2840px;background:#000" viewBox="0 0 1200 146" preserveAspectRatio="none">
  <polygon points="0,0 600,80 1200,0" fill="#f0f3f8"/>
  <polygon points="0,0 600,80 0,146" fill="#00A9DD"/>
  <polygon points="1200,0 600,80 1200,146" fill="#0054AA"/>
</svg>
<div class="round-arrow" style="left:576px;top:2894px">
  <svg width="16" height="18" viewBox="0 0 16 18"><path d="M8 16V3M3 8l5-5 5 5" fill="none" stroke="currentColor" stroke-width="1.6"/></svg>
</div>

<footer class="site-footer">
  <a class="footer-brand" href="#"><span class="brand-dot"></span>TB</a>
  <nav class="footer-nav">
    <a href="#">HOME</a><span class="sep">|</span>
    <a href="#">ABOUT US</a><span class="sep">|</span>
    <a href="#">OUR SERVICES</a><span class="sep">|</span>
    <a href="#">TESTIMONIALS</a><span class="sep">|</span>
    <a href="#">CONTACT US</a>
  </nav>
  <div class="footer-rule"></div>
  <div class="copyright">©2025. All rights reserved.</div>
</footer>

</body>
</html>
```